Natural Cosmetics need a Packaging Design

We need a PACKAGING design for labels on hand/body wash bottles and soap paper boxes.
We target at high end markets.
We expect a contemporary and trendy design.
We don't need a separate logo. The brand name "Ma Vitrine" acts as the logo.
We want a modern and classic font for "Ma Vitrine".
Please see attached pictures for packaging samples.

Industry/Entity Type

Cosmetics

Requirements
Should not have
• a separate logo from the brand name

```html
<!DOCTYPE html>
<html lang="en">
<head>
<meta charset="utf-8">
<title>Ma Vitrine — Packaging Labels</title>
<link rel="stylesheet" href="https://fonts.googleapis.com/css2?family=Cormorant+Garamond:ital,wght@0,400;1,400&family=Open+Sans:wght@600&display=swap">
<style>
  :root {
    --backdrop: #e4e4e6;
    --label: #fbfbfb;
    --label-edge: #e0e0e2;
    --accent: #6fd6c4;
    --ink: #4a4a4c;
    --ink-soft: #8a8a8e;
    --foil: #c4c6c9;
  }
  * { margin: 0; padding: 0; box-sizing: border-box; }
  html, body { width: 1200px; height: 900px; overflow: hidden; }
  body {
    background: var(--backdrop);
    position: relative;
    font-family: "Cormorant Garamond", Georgia, serif;
  }
  .label {
    position: absolute;
    background: var(--label);
    border: 1px solid var(--label-edge);
    display: flex;
    flex-direction: column;
    align-items: center;
    text-align: center;
    color: var(--ink);
  }
  .label--soap { left: 190px; top: 470px; width: 220px; height: 260px; border-radius: 8px; padding-top: 40px; color: var(--foil); }
  .label--body { left: 480px; top: 250px; width: 240px; height: 480px; border-radius: 40px; padding-top: 130px; }
  .label--hand { left: 790px; top: 450px; width: 230px; height: 280px; border-radius: 36px; padding-top: 44px; }

  .brand-dot { width: 44px; height: 44px; border-radius: 50%; background: var(--accent); }
  .label--soap .brand-dot { background: #bfeee6; }
  .brand-name {
    margin-top: 10px;
    font-size: 20px;
    letter-spacing: 0.18em;
    font-weight: 400;
    color: var(--ink-soft);
  }
  .label--soap .brand-name { color: var(--foil); }
  .product {
    font-family: "Open Sans", Arial, sans-serif;
    font-weight: 600;
    font-size: 14px;
    letter-spacing: 0.06em;
    margin-top: 48px;
  }
  .label--hand .product { margin-top: 8px; font-size: 15px; color: var(--ink-soft); }
  .scent { font-style: italic; font-size: 13px; letter-spacing: 0.12em; color: var(--ink-soft); }
  .label--soap .product, .label--soap .scent { color: var(--foil); }
  .tagline {
    margin-top: 70px;
    font-size: 8px;
    letter-spacing: 0.12em;
    line-height: 1.4;
    color: var(--ink-soft);
  }
  .label--hand .tagline { margin-top: 18px; }
  .label--soap .tagline { margin-top: 48px; color: var(--foil); }
  .volume {
    margin-top: auto;
    margin-bottom: 40px;
    font-family: "Open Sans", Arial, sans-serif;
    font-size: 9px;
    color: var(--ink-soft);
  }
  .label--hand .volume { margin-top: 18px; margin-bottom: 0; }
</style>
</head>
<body>
  <section class="label label--soap">
    <span class="brand-dot"></span>
    <h1 class="brand-name">Ma Vitrine</h1>
    <p class="product">soap</p>
    <p class="scent">grapefruit</p>
    <p class="tagline">naturaly essencial ingridients<br>balanced together</p>
  </section>

  <section class="label label--body">
    <span class="brand-dot"></span>
    <h2 class="brand-name">Ma Vitrine</h2>
    <p class="product">body wash</p>
    <p class="scent">rose</p>
    <p class="tagline">naturaly essencial ingridients<br>balanced together</p>
    <p class="volume">200 ml</p>
  </section>

  <section class="label label--hand">
    <span class="brand-dot"></span>
    <h2 class="brand-name">Ma Vitrine</h2>
    <p class="product">hand wash</p>
    <p class="scent">white tea</p>
    <p class="tagline">naturaly essencial ingridients<br>balanced together</p>
    <p class="volume">20 ml</p>
  </section>
</body>
</html>
```